Business Card Design Project

Please create a custom business card for Loftwell Capital. The logo is attached to this brief.

Also, here is the link to the logo design project: http://jobs.briskmotif.com/job.aspx?id=462035

Questions can be posted on the Discussion Board.

```html
<!DOCTYPE html>
<html lang="en">
<head>
<meta charset="utf-8">
<title>Loftwell Capital — Business Card</title>
<link rel="stylesheet" href="https://fonts.googleapis.com/css2?family=Mulish:ital,wght@0,400;0,600;1,400;1,800&display=swap">
<style>
  :root {
    --page: #ffffff;
    --card-face: #e1e9ea;
    --band-blue: #29a6e0;
    --panel-white: #f7f9fa;
    --ink: #3b4346;
    --ink-soft: #4a5256;
    --back-top: #1459b5;
    --back-bottom: #2592d4;
    --back-base: #4b5558;
  }
  * { box-sizing: border-box; margin: 0; padding: 0; }
  html, body {
    width: 1200px; height: 840px; overflow: hidden;
    background: var(--page);
    font-family: "Mulish", sans-serif;
  }
  .canvas { position: relative; width: 1200px; height: 840px; }
  .card {
    position: absolute; left: 280px; width: 640px; height: 355px; overflow: hidden;
  }
  .card-front { top: 45px; background: var(--card-face); }
  .card-back { top: 440px; background: linear-gradient(180deg, var(--back-top), var(--back-bottom)); }

  .band { position: absolute; left: 0; width: 100%; }
  .band-top { top: 0; height: 26px; background: var(--band-blue); }
  .band-bottom { bottom: 0; height: 11px; background: var(--band-blue); }
  .band-base { bottom: 0; height: 26px; background: var(--back-base); }

  .shape { position: absolute; left: 0; top: 0; }

  .brand {
    position: absolute; display: flex; flex-direction: column; align-items: center;
    color: var(--ink); font-weight: 600; text-align: center; line-height: 1.1;
  }
  .brand-square { width: 26px; height: 26px; background: var(--ink); margin-bottom: 12px; }
  .brand-name { font-size: 31px; letter-spacing: 2px; }
  .brand-sub { font-size: 17px; letter-spacing: 3px; margin-top: 2px; }
  .card-front .brand { left: 62px; top: 228px; width: 240px; }
  .card-back .brand { left: 200px; top: 126px; width: 260px; }
  .card-back .brand-name { font-size: 35px; }
  .card-back .brand-sub { font-size: 19px; }

  .holder { position: absolute; left: 357px; top: 50px; width: 240px; color: var(--ink); }
  .holder-name { font-size: 28px; font-weight: 800; font-style: italic; letter-spacing: -0.3px; }
  .holder-rule { height: 1px; background: var(--ink); width: 234px; margin-top: 8px; }
  .holder-role { font-size: 20px; font-style: italic; text-align: center; width: 234px; margin-top: 8px; color: var(--ink-soft); }

  .contacts {
    position: absolute; left: 358px; top: 146px; list-style: none;
    color: var(--ink-soft); font-size: 15px; font-style: italic;
  }
  .contacts li { display: flex; align-items: center; height: 26.5px; }
  .contacts svg { width: 16px; height: 16px; margin-right: 9px; fill: var(--ink); flex: none; }
</style>
</head>
<body>
<main class="canvas">

  <section class="card card-front" aria-label="Card front">
    <div class="band band-top"></div>
    <svg class="shape" width="640" height="355" viewBox="0 0 640 355" aria-hidden="true">
      <polygon points="176,74 340,344 22,344" fill="var(--panel-white)"/>
    </svg>
    <div class="band band-bottom"></div>

    <div class="brand">
      <span class="brand-square"></span>
      <span class="brand-name">LOFTWELL</span>
      <span class="brand-sub">CAPITAL</span>
    </div>

    <div class="holder">
      <p class="holder-name">Your&nbsp; Long Name</p>
      <div class="holder-rule"></div>
      <p class="holder-role">your position</p>
    </div>

    <ul class="contacts">
      <li>
        <svg viewBox="0 0 16 16"><path d="M8 1a5 5 0 0 0-5 5c0 3.6 5 9 5 9s5-5.4 5-9a5 5 0 0 0-5-5zm0 7a2 2 0 1 1 0-4 2 2 0 0 1 0 4z"/></svg>
        Street No.123&nbsp; Hometown
      </li>
      <li>
        <svg viewBox="0 0 16 16"><path d="M1 5c0-2 3-3 7-3s7 1 7 3v1h-3.5V4.5h-7V6H1zM3 8l2-2h6l2 2v6H3zm5 1.2a1.8 1.8 0 1 0 0 3.6 1.8 1.8 0 0 0 0-3.6z"/></svg>
        + 12.3456.7890
      </li>
      <li>
        <svg viewBox="0 0 16 16"><path d="M2 5h3V1h7l2 2v2h1v10H2zm4 0h6V3.5L11 2H6zM4 8v1.5h2V8zm3 0v1.5h2V8zm3 0v1.5h2V8zM4 11v1.5h2V11zm3 0v1.5h2V11zm3 0v1.5h2V11z"/></svg>
        + 12.3456.7890
      </li>
      <li>
        <svg viewBox="0 0 16 16"><path d="M5 1h6a1 1 0 0 1 1 1v12a1 1 0 0 1-1 1H5a1 1 0 0 1-1-1V2a1 1 0 0 1 1-1zm1 2v5h4V3zm0 6.5v1h1v-1zm1.5 0v1h1v-1zm1.5 0v1h1v-1zM6 11.5v1h1v-1zm1.5 0v1h1v-1zm1.5 0v1h1v-1z"/></svg>
        + 12.3456.7890
      </li>
      <li>
        <svg viewBox="0 0 16 16"><path d="M2 4h12v8H2zm1.2 1L8 8.6 12.8 5z"/></svg>
        yourname@company.com
      </li>
      <li>
        <svg viewBox="0 0 16 16"><path d="M8 2l7 6h-2v6H9.5v-4h-3v4H3V8H1z"/></svg>
        www.yourcompany.com
      </li>
    </ul>
  </section>

  <section class="card card-back" aria-label="Card back">
    <svg class="shape" width="640" height="355" viewBox="0 0 640 355" aria-hidden="true">
      <polygon points="409,33 542,329 207,329 128,158" fill="#ffffff"/>
    </svg>
    <div class="band band-base"></div>

    <div class="brand">
      <span class="brand-square"></span>
      <span class="brand-name">LOFTWELL</span>
      <span class="brand-sub">CAPITAL</span>
    </div>
  </section>

</main>
</body>
</html>
```